www.tlorvantix.com

We are a company that is in the business of extending the life of surgical equipment by repairing or refurbishing equipment to save hospitals, surgery centers and clinics money. We call ourselves Pelbrook Medical Corporation. We are in need of a website that delivers the "feel" of what of we do everyday. A website that explains our services but at the same time has a touch that is different from the rest. Many companies repair but their websites may not "pull" customers to inquire, we need that punch. At this time we are not looking for e-commerce but would like the option of adding that in the future. We do sell new and used equipment, so we like to be able to highlight those manufacturers on our site. We would like the website to have enough layouts for pictures to describe what we repair.
Target Market(s)
Biomedical Technicians and Managers, Hospital Purchasing Departments, OR Managers, type of facilities that our customer exists in, hospitals, surgery centers, clinics, animal hospitals
Industry/Entity Type
E-Commerce
Requirements
Must have
- An easy to navigate website, modern looking.
Easy to modify with pictures and or additional web pages
The winning designer to be available for future modifications and changes
Website to be unique compared to our competition, which are numerous
Nice to have
- E-Commerce capability

```html
<!DOCTYPE html>
<html lang="en">
<head>
<meta charset="utf-8">
<title>Pelbrook Medical Corporation</title>
<link href="https://fonts.googleapis.com/css2?family=Ubuntu:wght@300;400;500;700&display=swap" rel="stylesheet">
<style>
:root{
  --green:#5a9a1e;
  --green-bright:#6fb62c;
  --blue:#1f5f9e;
  --blue-dark:#164a80;
  --navy:#1b4f86;
  --text:#555;
  --muted:#777;
  --line:#e2e2e2;
  --band:#f3f3f3;
  --footer:#333;
  --footer-text:#bbb;
}
*{margin:0;padding:0;box-sizing:border-box}
html,body{width:952px;height:1200px;overflow:hidden;background:#fff}
body{font-family:"Ubuntu",sans-serif;color:var(--text)}
.page{position:relative;width:952px;height:1200px;overflow:hidden;background:#fff}

/* header */
.site-header{position:absolute;left:0;top:0;width:952px;height:110px;background:linear-gradient(#fff,#f7f7f7);border-bottom:1px solid #e6e6e6}
.brand{position:absolute;left:81px;top:22px;display:flex;align-items:center;gap:8px}
.brand-dot{width:34px;height:34px;border-radius:50%;background:var(--green-bright)}
.brand-text{font-size:30px;font-weight:500;color:var(--blue);line-height:1}
.brand-sub{position:absolute;left:81px;top:68px;font-size:9.5px;color:var(--blue);letter-spacing:.2px}
.topbar{position:absolute;right:79px;top:17px;display:flex;align-items:center;font-size:15px;color:#777}
.topbar .phone{color:var(--navy);font-weight:500;margin-left:4px}
.topbar .sep{margin:0 9px;color:#999}
.topbar .cart{color:var(--green);font-size:11px;display:flex;align-items:center;gap:5px}
.top-rule{position:absolute;left:510px;right:78px;top:48px;border-top:1px solid #e3e3e3}
.main-nav{position:absolute;left:510px;top:60px;display:flex;align-items:center;font-size:12.5px}
.main-nav a{color:#555;text-decoration:none;margin-right:32px}
.main-nav a.active{background:linear-gradient(#2a72b8,#15508e);color:#fff;padding:6px 13px;border-radius:2px;margin-right:21px}
.main-nav a:last-child{margin-right:0}

/* hero */
.hero{position:absolute;left:0;top:110px;width:952px;height:331px;background:linear-gradient(100deg,#e9eef1 0%,#cfdce6 30%,#9fc0da 55%,#5ba0d0 75%,#b8d0a2 90%,#d6dde2 100%)}
.hero-caption{position:absolute;left:551px;top:61px;width:321px;height:215px;background:rgba(255,255,255,.82);border-radius:3px;padding:17px 20px 0 20px;text-align:right;font-size:22.5px;font-weight:300;color:#333;line-height:35px}
.dots{position:absolute;right:20px;bottom:28px;display:flex;gap:7px}
.dots span{width:11px;height:11px;border-radius:50%;background:#999}
.dots span:first-child{background:#444}

/* content */
.intro{position:absolute;left:80px;top:465px;width:538px}
.section-title{font-size:22px;color:var(--green);font-weight:400;margin-bottom:9px}
.section-title.small{font-size:18px}
.body-copy{font-size:11px;line-height:20px;color:var(--text)}
.divider{border-top:1px solid var(--line);margin:19px 0 21px}
.service-links{display:grid;grid-template-columns:183px 176px 1fr;row-gap:5px;margin-top:12px;list-style:none;font-size:11px;color:var(--navy);font-weight:500}
.service-links li::before{content:"»";margin-right:6px;font-size:13px}

/* quick contact */
.quick-contact{position:absolute;left:646px;top:472px;width:228px;height:328px;background:linear-gradient(#2d74b7,#1a5593);border-radius:3px;padding:13px 10px 0 13px}
.qc-head{display:flex;align-items:center;gap:10px;color:#fff;font-size:22px;font-weight:300;margin-bottom:11px}
.qc-field{display:block;width:205px;height:30px;background:#f8f8f8;border-bottom:4px solid #e6e6e6;margin-bottom:12px;font-size:10.5px;color:#777;padding:8px 14px}
.qc-field.msg{height:88px}
.qc-submit{position:absolute;right:10px;top:282px;width:59px;height:28px;background:linear-gradient(#fafafa,#d9d9d9);color:#333;font-size:11px;font-weight:500;display:flex;align-items:center;justify-content:center;border-radius:2px}

/* products */
.products{position:absolute;left:0;top:833px;width:952px;height:185px;background:linear-gradient(#f1f1f1,#fff 60%)}
.products .section-title{position:absolute;left:87px;top:20px;font-size:18px}
.carousel-nav{position:absolute;left:838px;top:25px;display:flex;gap:2px}
.carousel-nav span{width:13px;height:13px;border-radius:50%;background:#ddd;font-size:8px;color:#666;display:flex;align-items:center;justify-content:center}
.product-card{position:absolute;top:57px;width:180px;height:113px;background:#f9f9f9;border:1px solid #ddd}
.product-photo{position:absolute;inset:12px 45px;background:radial-gradient(#d4dbe2,#f9f9f9 70%)}
.product-card.featured{background:linear-gradient(#5a83b4,#3f6aa0);border-color:#3a6398}
.product-card.featured .label{position:absolute;left:0;right:0;top:32px;text-align:center;color:#fff;font-size:17px;font-weight:500}
.product-card.featured svg{position:absolute;left:77px;top:62px}

/* partners */
.partners{position:absolute;left:80px;top:1032px;width:794px;border-top:1px solid var(--line);display:flex;justify-content:space-between;align-items:center;padding:23px 12px 0;font-size:17px;color:#8a8a8a;font-weight:500}

/* footer */
.site-footer{position:absolute;left:0;top:1107px;width:952px;height:93px;background:var(--footer)}
.footer-nav{position:absolute;left:80px;top:23px;font-size:11.5px;color:var(--footer-text)}
.footer-nav span{margin:0 7px;color:#888}
.copyright{position:absolute;left:80px;top:52px;font-size:11.5px;color:var(--footer-text)}
.social{position:absolute;left:769px;top:34px;display:flex;gap:8px}
.social span{width:20px;height:20px;border-radius:50%;background:var(--green-bright);display:flex;align-items:center;justify-content:center}
</style>
</head>
<body>
<div class="page">

  <header class="site-header">
    <div class="brand"><span class="brand-dot"></span><span class="brand-text">Pelbrook</span></div>
    <div class="brand-sub">PELBROOK MEDICAL · EQUIPMENT SUSTAINABILITY SOLUTIONS</div>
    <div class="topbar">
      <svg width="16" height="14" viewBox="0 0 16 14" aria-hidden="true"><path d="M3 1 L6 1 L7 4 L5 5.5 Q7 9 10.5 10 L12 8 L15 9 L15 12 Q14 13.5 12 13 Q4 11 2 3 Q2 1.5 3 1Z" fill="#999"/></svg>
      <span style="margin-left:6px">Call us :</span><span class="phone">262-555-0148</span>
      <span class="sep">|</span>
      <span class="cart"><svg width="16" height="14" viewBox="0 0 16 14" aria-hidden="true"><path d="M1 1h2.5l2 8h8l2-6H4.5" fill="none" stroke="#5a9a1e" stroke-width="1.6"/><circle cx="6.5" cy="12" r="1.3" fill="#5a9a1e"/><circle cx="12.5" cy="12" r="1.3" fill="#5a9a1e"/></svg>My Cart &nbsp;(0) items</span>
    </div>
    <div class="top-rule"></div>
    <nav class="main-nav">
      <a class="active" href="#">Home</a><a href="#">About us</a><a href="#">Services</a><a href="#">Products</a><a href="#">Contact us</a>
    </nav>
  </header>

  <section class="hero" role="img" aria-label="Hospital corridor with surgical staff in blue scrubs walking past medical equipment">
    <div class="hero-caption">We repair and refurbishing equipment to save hospitals, surgery centers and clinics money.
      <div class="dots"><span></span><span></span><span></span><span></span></div>
    </div>
  </section>

  <main class="intro">
    <h1 class="section-title">Welcome to Pelbrook</h1>
    <p class="body-copy">Suspendisse congue, nisl quis posuere pretium, risus tellus posuere velit, sed placerat turpis lacus condi mentum mi. Fusce semper eleifend orci sit amet consectetur. Nulla sed massa sagittis, tristique felis nec, egestas leo. Duis facilisis suscipit convallis. Interdum et malesuada fames ac ante ipsum primis in faucibus. In dapibus nisi at felis tincidunt, sit amet semper est sagittis. Suspendisse magna augue, sollicitudin vulpu tate blandit et, sagittis vitae ipsumvel tempor velit, sed accumsan ligula.</p>
    <div class="divider"></div>
    <h2 class="section-title small">Our Services</h2>
    <p class="body-copy">Suspendisse congue, nisl quis posuere pretium, risus tellus posuere velit, sed placerat turpis lacus condi mentum mi. Fusce semper eleifend orci sit amet consectetur. Nulla sed massa sagittis, tristique felis nec, egestas leo. Duis facilisis suscipit convallis. Interdum et malesuada fames ac ante ipsum primis in faucibus.</p>
    <ul class="service-links">
      <li>Nam nisl enim, ultricies</li><li>Vivamus consectetur</li><li>Fusce aliquam urna</li>
      <li>Etiam vel tempor velit</li><li>Donec lobortis hendrerit</li><li>Cum sociis</li>
      <li>Morbi porttitorsem</li><li>Suspendisse</li><li>Nulla pellentesque condimentum</li>
    </ul>
  </main>

  <aside class="quick-contact">
    <div class="qc-head">
      <svg width="32" height="32" viewBox="0 0 32 32" aria-hidden="true"><circle cx="16" cy="16" r="15" fill="#e8f0f7"/><path d="M10 8h4l1.5 4-2.5 2q2 4 5 5l2-2.5 4 1.5v4q-1 2-3 2Q12 23 9 11q0-2 1-3Z" fill="#1f5f9e"/></svg>
      Quick Contact
    </div>
    <span class="qc-field">Name</span>
    <span class="qc-field">E-mail</span>
    <span class="qc-field">Phone</span>
    <span class="qc-field msg">Message</span>
    <span class="qc-submit">SUBMIT</span>
  </aside>

  <section class="products">
    <h2 class="section-title">Our Products</h2>
    <div class="carousel-nav"><span>‹</span><span>›</span></div>
    <div class="product-card featured" style="left:88px" role="img" aria-label="Stethoscope product">
      <div class="label">Product name</div>
      <svg width="26" height="20" viewBox="0 0 26 20" aria-hidden="true"><path d="M1 2h4l3 11h13l3-8H6" fill="none" stroke="#fff" stroke-width="2"/><circle cx="10" cy="17" r="2" fill="#fff"/><circle cx="19" cy="17" r="2" fill="#fff"/></svg>
    </div>
    <div class="product-card" style="left:287px"><div class="product-photo" role="img" aria-label="X-ray table system"></div></div>
    <div class="product-card" style="left:486px"><div class="product-photo" role="img" aria-label="Hospital stretcher bed"></div></div>
    <div class="product-card" style="left:686px"><div class="product-photo" role="img" aria-label="CT scanner"></div></div>
  </section>

  <div class="partners">
    <span>Halverton</span><span>Quenby</span><span>Tressly</span><span>Orvel</span><span>Daxmoor</span><span>Ruvo</span><span>Fenwyck</span><span>Alvara</span><span>Brindle</span>
  </div>

  <footer class="site-footer">
    <div class="footer-nav">Home<span>|</span>About us<span>|</span>Services<span>|</span>Products<span>|</span>Contact us</div>
    <div class="copyright">copyright &nbsp;©&nbsp; 2013 &nbsp;&nbsp; Pelbrook corp. &nbsp; All rights reserved.</div>
    <div class="social">
      <span></span><span></span><span></span>
      <span><svg width="11" height="8" viewBox="0 0 11 8" aria-hidden="true"><rect x=".5" y=".5" width="10" height="7" fill="none" stroke="#fff"/><path d="M.5 .5l5 4 5-4" fill="none" stroke="#fff"/></svg></span>
    </div>
  </footer>

</div>
</body>
</html>
```